Business / Discount Card

Looking to create a 2 sided business card. Front side to say "Thanks for flying with Skyward Drifts" then have link to "In-Flight Photos, www.skywarddrifts-example.com.au, password: skyward" Back side of card to have company logo, phone number, facebook & instagram logo and #skywarddrifts. Also included on this side will be discount text "Book again and save 10%. Use discount code: skyward10"Round Corner Card Templates are attached. Please ensure dimensions are correct.Thanks,

Font styles to use
Sans Serif

Colors
33a6d7
ffffff
000000

Requirements
Must have
• Logo
• Blue, White and Black color scheme

```html
<!DOCTYPE html>
<html lang="en">
<head>
<meta charset="utf-8">
<title>Skyward Drifts – Business / Discount Card</title>
<link href="https://fonts.googleapis.com/css2?family=Lato:ital,wght@0,400;0,700;1,400&family=Open+Sans:ital,wght@0,400;0,700;1,700&family=Oswald:wght@400&display=swap" rel="stylesheet">
<style>
  :root {
    --sky-blue: #00aeef;
    --brand-blue: #33a6d7;
    --ink: #000000;
    --paper: #ffffff;
    --paper-shade: #eeeeee;
    --backdrop: #e4e1de;
    --ghost: #c9c9c9;
  }
  * { margin: 0; padding: 0; box-sizing: border-box; }
  html, body {
    width: 1200px; height: 991px; overflow: hidden;
    background: var(--backdrop);
  }
  .canvas { position: relative; width: 1200px; height: 991px; }

  .card {
    position: absolute;
    background: linear-gradient(180deg, var(--paper) 0%, var(--paper-shade) 100%);
    box-shadow: 0 6px 18px rgba(0,0,0,0.18);
    overflow: hidden;
  }

  /* Discount side */
  .card--discount { left: 208px; top: 115px; width: 567px; height: 351px; }
  .card--discount .brand-name {
    position: absolute; left: 0; right: 0; top: 98px;
    text-align: center;
    font-family: "Open Sans", sans-serif; font-weight: 700;
    font-size: 46px; color: var(--sky-blue); letter-spacing: -0.5px;
  }
  .card--discount .rule {
    position: absolute; left: 0; right: 0; top: 194px; height: 6px;
    background: var(--sky-blue);
  }
  .card--discount .panel {
    position: absolute; left: 0; right: 0; top: 200px; bottom: 0;
    background: var(--ink); color: var(--paper);
    font-family: "Open Sans", sans-serif;
  }
  .phone {
    position: absolute; left: 33px; top: 36px;
    font-family: "Oswald", sans-serif; font-size: 33px; line-height: 1;
    color: var(--sky-blue); letter-spacing: 0.2px;
  }
  .offer {
    position: absolute; left: 34px; top: 96px;
    font-size: 18px;
  }
  .social {
    position: absolute; right: 31px; top: 37px;
    display: flex; align-items: center; gap: 6px;
    font-size: 16px;
  }
  .social .dot {
    width: 25px; height: 25px; border-radius: 50%;
    background: #3b5998;
  }
  .social .label { margin-right: 4px; }
  .code {
    position: absolute; right: 31px; top: 76px; text-align: right;
    line-height: 1.3;
  }
  .code .lead { font-size: 19px; color: var(--sky-blue); }
  .code .value { font-size: 20px; font-weight: 700; font-style: italic; letter-spacing: 0.5px; }

  /* Thanks side */
  .card--thanks { left: 438px; top: 508px; width: 577px; height: 357px; }
  .card--thanks .brand-ghost {
    position: absolute; left: 0; right: 0; top: 90px;
    text-align: center;
    font-family: "Lato", sans-serif; font-weight: 700;
    font-size: 44px; color: var(--ghost);
  }
  .card--thanks .rule {
    position: absolute; left: 0; right: 0; top: 198px; height: 6px;
    background: var(--ink);
  }
  .card--thanks .panel {
    position: absolute; left: 0; right: 0; top: 204px; bottom: 0;
    background: var(--sky-blue); color: var(--paper);
    font-family: "Lato", sans-serif; text-align: center;
  }
  .thanks-line {
    position: absolute; left: 0; right: 0; top: 24px;
    font-size: 17.5px; font-weight: 700; letter-spacing: 0.1px;
  }
  .photo-access {
    position: absolute; left: 0; right: 0; top: 66px; line-height: 1.2;
  }
  .photo-access .title { font-size: 18px; }
  .photo-access .url { font-size: 20px; font-weight: 700; }
  .photo-access .pass { font-size: 16.5px; font-style: italic; }
</style>
</head>
<body>
<main class="canvas">

  <section class="card card--discount" aria-label="Discount side of card">
    <div class="brand-name">Skyward Drifts</div>
    <div class="rule"></div>
    <div class="panel">
      <div class="phone">044-555 010 247</div>
      <div class="offer">Book again and save 10%</div>
      <div class="social">
        <span class="label">#skywarddrifts</span>
        <span class="dot" aria-hidden="true"></span>
        <span class="dot" aria-hidden="true"></span>
      </div>
      <div class="code">
        <div class="lead">Use discount code:</div>
        <div class="value">SKYWARD10</div>
      </div>
    </div>
  </section>

  <section class="card card--thanks" aria-label="Thank-you side of card">
    <div class="brand-ghost" aria-hidden="true">Skyward Drifts</div>
    <div class="rule"></div>
    <div class="panel">
      <div class="thanks-line">THANKS FOR FLYING WITH SKYWARD DRIFTS</div>
      <div class="photo-access">
        <div class="title">In-Flight Photo</div>
        <div class="url">www.skywarddrifts-example.com.au</div>
        <div class="pass">password: skyward</div>
      </div>
    </div>
  </section>

</main>
</body>
</html>
```